Simple Business Card Design for Foodie

Job:

Make a very simple, minimalist business card design with my details including adjusted logo. One side to be white (with logo & text). Other side to be yellow - try plain or with logo (or part of logo eg Z). Need business card to have continuity with website.

Logo:
Our logo is made from a free download font website:
http://www.typegrotto.net/search.php?q=rubber
but the spacing/kerning needs correcting/adjusting as the font spaces unevenly between letters (see attached files). Need logo to be very crisp/sharp when printed.

Printing:
We will be using Kelvo.com so the design needs to conform to their requirements, see here:

http://uk.kelvo.com/products/velour/business-cards.html (scroll down for dimensions and guidelines)

Design:

must say "plant-based food consulting" underneath logo or somewhere
no address needed in contact section
sharp corners (not rounded)
one side white, one side yellow

name: Harriet Colwick
1xmobile number: +44 7700900461
1xtwiiter: @pelkoadvice
website address www.marrowlanekitchen.com
email address pelko@marrowlanekitchen.com

Should be easy quick job, prompt + detailed feedback given, am online in UK 9am-10pm for next 3 days. Website is www.marrowlanekitchen.com

Industry/Entity Type

Business

Requirements
Must have
• The logo must be corrected. The kerning is not right.

Please use a warm-grey for text

Please submit in matt format, we will be printing matt finish.

Should not have
• Avoid using banners or curvy highlights

Please avoid using black

Please avoid submitting in gloss finish

```html
<!DOCTYPE html>
<html lang="en">
<head>
<meta charset="utf-8">
<title>Pelko — Business Card</title>
<link rel="stylesheet" href="https://fonts.googleapis.com/css2?family=Arimo&family=Open+Sans:wght@700&family=Questrial&display=swap">
<style>
  :root {
    --backdrop: #e9e8e6;
    --card: #ffffff;
    --brand-yellow: #e9d629;
    --warm-grey: #545250;
    --divider: #c9c6c2;
  }
  * { box-sizing: border-box; margin: 0; padding: 0; }
  html, body {
    width: 1200px;
    height: 1000px;
    overflow: hidden;
    background: var(--backdrop);
  }
  .business-card {
    position: absolute;
    left: 135px;
    top: 193px;
    width: 938px;
    height: 614px;
    overflow: hidden;
    background: var(--card);
    box-shadow: 0 2px 6px rgba(0,0,0,0.12);
  }
  .brand-name {
    position: absolute;
    right: 560px;
    top: 178px;
    font-family: "Questrial", sans-serif;
    font-size: 97px;
    line-height: 1;
    letter-spacing: 0;
    white-space: nowrap;
    color: var(--brand-yellow);
  }
  .tagline {
    position: absolute;
    right: 560px;
    top: 375px;
    font-family: "Arimo", sans-serif;
    font-size: 23.5px;
    line-height: 27px;
    text-align: right;
    color: var(--warm-grey);
  }
  .divider {
    position: absolute;
    left: 441px;
    top: 185px;
    width: 1px;
    height: 209px;
    background: var(--divider);
  }
  .person-name {
    position: absolute;
    left: 506px;
    top: 174px;
    font-family: "Open Sans", sans-serif;
    font-weight: 700;
    font-size: 30px;
    letter-spacing: 0.5px;
    color: var(--warm-grey);
  }
  .contact-list {
    position: absolute;
    left: 504px;
    top: 260px;
    list-style: none;
  }
  .contact-item {
    display: flex;
    align-items: center;
    height: 34.75px;
    font-family: "Questrial", sans-serif;
    font-size: 23px;
    white-space: nowrap;
    color: var(--warm-grey);
  }
  .contact-icon {
    width: 24px;
    height: 24px;
    margin-right: 12px;
    flex: none;
  }
  .contact-icon * {
    fill: none;
    stroke: var(--brand-yellow);
    stroke-width: 1.8;
    stroke-linecap: round;
    stroke-linejoin: round;
  }
</style>
</head>
<body>
  <section class="business-card">
    <div class="brand-name">PELKO</div>
    <p class="tagline">PLANT-BASED<br>FOOD CONSULTING</p>

    <div class="divider"></div>

    <h1 class="person-name">HARRIET COLWICK</h1>

    <ul class="contact-list">
      <li class="contact-item">
        <svg class="contact-icon" viewBox="0 0 24 24" aria-hidden="true">
          <circle cx="12" cy="12" r="10.5"/>
          <path d="M8.6 6.8l1.8 2.4-1 1.3c.8 1.7 2.1 3 3.8 3.8l1.3-1 2.4 1.8-.9 1.7c-4.2-.4-8.2-4.4-8.6-8.6z"/>
        </svg>
        +44 7700900461
      </li>
      <li class="contact-item">
        <svg class="contact-icon" viewBox="0 0 24 24" aria-hidden="true">
          <circle cx="12" cy="12" r="10.5"/>
        </svg>
        @pelkoadvice
      </li>
      <li class="contact-item">
        <svg class="contact-icon" viewBox="0 0 24 24" aria-hidden="true">
          <circle cx="12" cy="12" r="10.5"/>
        </svg>
        pelkoadvice
      </li>
      <li class="contact-item">
        <svg class="contact-icon" viewBox="0 0 24 24" aria-hidden="true">
          <circle cx="12" cy="12" r="10.5"/>
          <rect x="6.5" y="8" width="11" height="8"/>
          <path d="M6.5 8l5.5 4.5L17.5 8"/>
        </svg>
        pelko@marrowlanekitchen.com
      </li>
      <li class="contact-item">
        <svg class="contact-icon" viewBox="0 0 24 24" aria-hidden="true">
          <circle cx="12" cy="12" r="10.5"/>
          <ellipse cx="12" cy="12" rx="4.5" ry="10.5"/>
          <path d="M1.5 12h21M3 7h18M3 17h18"/>
        </svg>
        www.marrowlanekitchen.com
      </li>
    </ul>
  </section>
</body>
</html>
```